Small Business Consulting Firm Needs Business Card Design

Need a sleek modern business card with 2 sides matching the colors of our logo. We will be placing these with a mailer we are sending out. These business cards will only ever be given to business owners. We operate helping businesses who are struggling with cash flow or finances. If the green and blue design needs to be moved to the right of "Harborline Crest Consulting" for aesthetic purposes that is ok. We will need an editable file if possible. We would like to include the reps name, email, website, and phone number. For now just use Peter Vance, pvance@harborlinecrest.com, www.harborlinecrest.com, and 833-555-0172.

```html
<!DOCTYPE html>
<html lang="en">
<head>
<meta charset="utf-8">
<title>Harborline Crest Consulting – Business Card</title>
<link rel="stylesheet" href="https://fonts.googleapis.com/css2?family=Questrial&family=Source+Sans+3:wght@400;600&display=swap">
<style>
  :root {
    --backdrop: #cbcfd2;
    --card: #ffffff;
    --ink: #4a4a4c;
    --green: #7bb043;
    --blue: #2f7bbf;
    --tint: #eef2e8;
  }
  * { margin: 0; padding: 0; box-sizing: border-box; }
  html, body { width: 1200px; height: 1200px; overflow: hidden; }
  body { background: var(--backdrop); position: relative; font-family: "Source Sans 3", sans-serif; }

  .card {
    position: absolute;
    left: 250px;
    width: 700px;
    height: 400px;
    background: var(--card);
    overflow: hidden;
  }
  .card--front { top: 146px; }
  .card--back { top: 652px; }

  .brand { position: absolute; text-align: center; font-family: "Questrial", sans-serif; font-weight: 400; color: var(--ink); }
  .brand__mark { display: block; margin: 0 auto; background: var(--green); }
  .brand__name { display: block; white-space: nowrap; letter-spacing: 0.08em; line-height: 1; }
  .brand__tag { display: block; white-space: nowrap; letter-spacing: 0.55em; line-height: 1; }

  .card--front .brand { left: 187px; top: 136px; transform: translateX(-50%); }
  .card--front .brand__mark { width: 72px; height: 72px; margin-bottom: 24px; }
  .card--front .brand__name { font-size: 23px; }
  .card--front .brand__tag { font-size: 12.5px; margin-top: 10px; padding-left: 0.55em; }

  .divider { position: absolute; left: 343px; top: 137px; width: 1.5px; height: 122px; background: var(--green); }

  .contact { position: absolute; left: 368px; top: 134px; }
  .contact__name { font-weight: 600; font-size: 28px; color: var(--green); letter-spacing: 0.01em; line-height: 1; }
  .contact__list { list-style: none; margin-top: 30px; }
  .contact__item { display: flex; align-items: center; height: 26px; font-size: 20.5px; color: var(--ink); }
  .contact__icon { width: 19px; height: 19px; margin-right: 10px; flex: none; fill: var(--blue); }

  .backdrop-square { position: absolute; left: 0; top: 111px; width: 286px; height: 289px; background: var(--tint); opacity: 0.8; }

  .card--back .brand { left: 514px; top: 108px; transform: translateX(-50%); }
  .card--back .brand__mark { width: 110px; height: 110px; margin-bottom: 24px; }
  .card--back .brand__name { font-size: 29px; }
  .card--back .brand__tag { font-size: 15px; margin-top: 12px; padding-left: 0.55em; }
</style>
</head>
<body>

<section class="card card--front">
  <div class="brand">
    <span class="brand__mark"></span>
    <span class="brand__name">HARBORLINE CREST</span>
    <span class="brand__tag">CONSULTING</span>
  </div>

  <div class="divider"></div>

  <div class="contact">
    <p class="contact__name">PETER VANCE</p>
    <ul class="contact__list">
      <li class="contact__item">
        <svg class="contact__icon" viewBox="0 0 24 24" aria-hidden="true"><path d="M6.6 10.8c1.4 2.8 3.8 5.1 6.6 6.6l2.2-2.2c.3-.3.7-.4 1-.2 1.1.4 2.3.6 3.6.6.6 0 1 .4 1 1V20c0 .6-.4 1-1 1C10.6 21 3 13.4 3 4c0-.6.4-1 1-1h3.5c.6 0 1 .4 1 1 0 1.3.2 2.5.6 3.6.1.3 0 .7-.2 1z"/></svg>
        833-555-0172
      </li>
      <li class="contact__item">
        <svg class="contact__icon" viewBox="0 0 24 24" aria-hidden="true"><path d="M2 5h20v14H2z M3.5 6.5l8.5 7 8.5-7v1.8l-5.5 4.5 5.5 4.7v.5h-1l-5.5-4.6L12 16l-2-1.6-5.5 4.6h-1v-.5l5.5-4.7-5.5-4.5z" fill-rule="evenodd"/></svg>
        pvance@harborlinecrest.com
      </li>
      <li class="contact__item">
        <svg class="contact__icon" viewBox="0 0 24 24" aria-hidden="true"><circle cx="12" cy="12" r="10"/><path d="M8 6c2 1 1 3 3 3s1 3-1 3-3 2-2 4M15 5c-1 2 1 3 3 3M17 14c-2 0-3 2-2 4" stroke="#fff" stroke-width="1.6" fill="none"/></svg>
        www.harborlinecrest.com
      </li>
    </ul>
  </div>
</section>

<section class="card card--back">
  <div class="backdrop-square"></div>
  <div class="brand">
    <span class="brand__mark"></span>
    <span class="brand__name">HARBORLINE CREST</span>
    <span class="brand__tag">CONSULTING</span>
  </div>
</section>

</body>
</html>
```